Investment fund website overhaul for modern aesthetic (example sites in description)

I would like to request an overhaul of our current website (www.silverbrookmeridianholdings.com), which craftly.net builders initially designed. The goal is to update the site's look and functionality while maintaining most of the existing page structure. Specifically, I'd like to implement the following changes:

Visual Redesign:
Please redesign the site to more closely resemble the style and aesthetic of the following three websites:
https://www.velmora.com/
https://www.tzq.com/
https://harborlynpartners.com/

New Portfolio, Meet the team, News & Insights:
Add a new "Portfolio" page to showcase our acquired businesses and properties. As we currently don't have any acquisitions, please include a "Coming Soon" message or placeholder content that explains our acquisition strategy and future plans.

Client Portal (a log in function):
Implement a secure client portal with the following features:
User authentication (username and password)
Ability for us to assign login credentials to investors
A personalized dashboard for each investor, displaying:
Their investments (API to come in the next several months)
Relevant legal documents
Personal information
Payment transfer (ACH/Wire/crypto)

Existing Pages:
Maintain the current site structure and content for existing pages but update their design to match the new aesthetic from those 3 websites.
Potentially change the names and additional pages (Who we are, What we do, Meet the Team, Our portfolio, News & Insights and then a separate client portal tab that sends them to a login in screen)

Please provide an estimate for these changes and a proposed timeline for completion. If you have any questions or need further clarification, please don't hesitate to ask.

Target Market(s)

Investors

Industry/Entity Type

AI, blockchain, digital assets, finance, and banking

Coding

Coded - Design and coding required

Number of Pages Required

5+ page

Colors

Designer to choose colors to be used in the design.

Requirements
Must have
• Pages: Who we are (landing/home page); What we do (mission page; Meet the team (coming soon); and Portfolio (Content coming soon)
Nice to have
• Client portal would be nice to have, but a simple but with the option and login credential page is fine for the time being.

```html
<!DOCTYPE html>
<html lang="en">
<head>
<meta charset="utf-8">
<title>Silverbrook Meridian Holdings, LLC</title>
<link href="https://fonts.googleapis.com/css2?family=Mulish:wght@300;400;600;700&family=Open+Sans:wght@700&family=Montserrat:wght@500;600&display=swap" rel="stylesheet">
<style>
:root{
  --navy:#0c1d3d;
  --gold:#c9a23f;
  --gold-soft:#e2b647;
  --ink:#1f2533;
  --muted:#444b5a;
  --footer-bg:#eef0f7;
  --white:#ffffff;
  --line:#8a93a8;
}
*{box-sizing:border-box;margin:0;padding:0}
html,body{width:1200px;height:4095px;overflow:hidden}
body{font-family:'Mulish',sans-serif;color:var(--ink);background:var(--white);position:relative}
section,header,footer{position:absolute;left:0;width:1200px}
.abs{position:absolute}
.btn{position:absolute;display:flex;align-items:center;justify-content:center;border:1px solid var(--gold);border-left-width:2px;font-family:'Montserrat',sans-serif;font-weight:500;font-size:12px;letter-spacing:2px;text-transform:uppercase;color:var(--ink)}
.btn.light{color:var(--white)}
.photo{position:absolute}

/* hero */
.hero{top:0;height:658px;background:linear-gradient(120deg,#3b3e44 0%,#5c5f63 40%,#2c2f35 75%,#4a4a48 100%)}
.hero-shade{position:absolute;inset:0;background:linear-gradient(90deg,rgba(10,14,22,.55),rgba(10,14,22,.15))}
.brand{position:absolute;left:86px;top:24px;display:flex;align-items:center;gap:10px}
.brand-mark{width:44px;height:44px;background:var(--gold)}
.brand-name{font-family:'Mulish',sans-serif;font-weight:600;font-size:12.5px;line-height:14px;letter-spacing:.6px;color:var(--white);text-transform:uppercase}
.nav{position:absolute;top:40px;font-size:15.5px;color:var(--white);letter-spacing:-.2px}
.hero h1{position:absolute;left:80px;top:246px;font-family:'Open Sans',sans-serif;font-weight:700;font-size:43px;line-height:53px;color:var(--white)}
.hero h1 span{color:var(--gold)}
.arrow{position:absolute;top:574px}

/* about */
.about{top:658px;height:658px}
.about h2{position:absolute;left:612px;top:146px;width:520px;font-weight:300;font-size:40px;line-height:49px;letter-spacing:-1px;color:var(--ink)}
.about p{position:absolute;left:612px;top:266px;width:480px;font-size:14.5px;line-height:24px;color:var(--muted)}

/* acquisitions */
.acquire{top:1316px;height:658px;background:var(--navy);color:var(--white)}
.acquire h2{position:absolute;left:84px;top:96px;font-weight:300;font-size:38px;line-height:47px;letter-spacing:-1px}
.acquire .lead{position:absolute;left:642px;top:106px;width:470px;font-size:14.5px;line-height:26px}
.focus-card{position:absolute;top:244px;width:504px;height:315px;border:1px solid var(--line);border-right:none}
.focus-card::after{content:"";position:absolute;right:0;top:0;width:1px;height:260px;background:var(--line)}
.focus-card .photo{left:15px;top:15px;width:474px;height:222px}
.focus-card h3{position:absolute;left:0;right:0;top:240px;text-align:center;font-weight:400;font-size:22px;line-height:33px;letter-spacing:-.6px}

/* services */
.services{top:1974px;height:658px}
.service{position:absolute;top:133px;width:248px}
.service .frame{position:relative;height:193px;border:1px solid #9aa0ac;border-top:none;border-right:none}
.service .frame::before{content:"";position:absolute;right:0;top:0;width:1px;height:193px;background:#9aa0ac}
.service .frame::after{content:"";position:absolute;left:0;top:0;width:10px;height:1px;background:#9aa0ac}
.service .photo{left:11px;top:8px;width:226px;height:178px}
.service h3{position:absolute;top:225px;left:0;width:250px;font-weight:400;font-size:17px;line-height:22px;letter-spacing:-.4px}
.service p{position:absolute;left:3px;width:240px;font-size:13.5px;line-height:24px;color:var(--muted)}
.service .btn{left:0;top:365px;width:155px;height:45px}

/* news */
.news{top:2632px;height:658px;background:var(--navy);color:var(--white)}
.news h2{position:absolute;left:84px;top:180px;font-weight:300;font-size:40px;letter-spacing:-1px}
.rule{position:absolute;height:2px;background:var(--white)}
.news .lead{position:absolute;left:86px;top:288px;width:305px;font-size:14.5px;line-height:25.5px}
.post{position:absolute;top:124px;width:320px}
.post .edge{position:absolute;left:10px;top:0;width:300px;height:209px;border:1px solid var(--line);border-bottom:none;border-left:none}
.post .photo{left:0;top:8px;width:300px;height:201px}
.post time{position:absolute;top:244px;left:0;font-size:11px;color:var(--gold-soft)}
.post h3{position:absolute;top:258px;left:0;width:320px;font-weight:700;font-size:17px;line-height:27px}
.post p{position:absolute;top:322px;left:0;width:320px;font-size:13.5px;line-height:24px;color:#dfe3ec}
.post .more{position:absolute;top:410px;left:0;font-family:'Montserrat',sans-serif;font-weight:500;font-size:12.5px;letter-spacing:1.8px;padding-bottom:4px;border-bottom:1px solid var(--white)}

/* cta */
.cta{top:3290px;height:298px;background:var(--gold-soft)}
.cta h2{position:absolute;left:262px;top:80px;font-weight:300;font-size:38px;letter-spacing:-1px;color:var(--ink)}
.cta .rule{background:var(--ink);left:262px;top:145px;width:96px}
.cta p{position:absolute;left:262px;top:172px;width:500px;font-size:14.5px;line-height:24px;color:var(--ink)}

/* footer */
.site-footer{top:3588px;height:507px;background:var(--footer-bg)}
.fcol{position:absolute;top:102px}
.fcol h4{font-weight:700;font-size:12.5px;letter-spacing:.6px;text-transform:uppercase;color:var(--ink)}
.fcol h4::after{content:"";display:block;width:28px;height:2px;background:var(--gold);margin-top:7px}
.fcol ul{list-style:none;margin-top:20px}
.fcol li{font-size:13px;line-height:32.6px;color:var(--ink)}
.email{position:absolute;left:822px;top:160px;width:292px;height:44px;border:1px solid #c9cdd8;background:var(--white);font-size:13px;color:#7d8494;padding:14px 16px}
.subscribe{position:absolute;left:822px;top:215px;width:292px;height:44px;background:var(--gold-soft);display:flex;align-items:center;justify-content:center;font-family:'Montserrat',sans-serif;font-weight:600;font-size:12.5px;letter-spacing:1.5px;color:var(--ink)}
.site-footer .brand{top:350px;left:84px}
.site-footer .brand-name{color:var(--ink)}
.connect{position:absolute;top:366px;left:566px;display:flex;gap:18px;font-size:12.5px;letter-spacing:.4px;color:var(--ink)}
.social{position:absolute;top:365px;left:1033px;display:flex;gap:16px}
.social span{width:15px;height:15px;border-radius:50%;background:var(--gold)}
.legal{position:absolute;top:459px;left:84px;font-size:12px;color:var(--muted)}
.legal b{color:var(--gold);font-weight:600}
</style>
</head>
<body>

<header class="hero">
  <div class="photo hero-shade" role="img" aria-label="Business team gathered around a laptop in a modern glass office"></div>
  <div class="brand">
    <span class="brand-mark"></span>
    <span class="brand-name">Silverbrook Meridian<br>Holdings, LLC</span>
  </div>
  <nav>
    <span class="nav" style="left:432px">Home</span>
    <span class="nav" style="left:500px">Who We Are</span>
    <span class="nav" style="left:617px">What We Do</span>
    <span class="nav" style="left:736px">Portfolio</span>
    <span class="nav" style="left:823px">Meet The Team</span>
    <span class="btn light" style="left:958px;top:29px;width:154px;height:44px">Client Portal</span>
  </nav>
  <h1>Where Technology Meets<br><span>Strategic Investment</span></h1>
  <span class="btn light" style="left:86px;top:378px;width:154px;height:45px">Our Mission</span>
  <svg class="arrow" style="left:86px" width="44" height="16" viewBox="0 0 44 16"><path d="M44 8H2M9 1L2 8l7 7" fill="none" stroke="#ffffff" stroke-width="1.6"/></svg>
  <svg class="arrow" style="left:140px" width="40" height="16" viewBox="0 0 40 16"><path d="M0 8h38M31 1l7 7-7 7" fill="none" stroke="#c9a23f" stroke-width="1.6"/></svg>
</header>

<section class="about">
  <svg class="abs" style="left:84px;top:118px" width="490" height="440" viewBox="0 0 490 440">
    <polyline points="478,0 484,0 484,330 390,428 14,428 14,400" fill="none" stroke="#c9a23f" stroke-width="2"/>
  </svg>
  <div class="photo" style="left:84px;top:119px;width:478px;height:421px;background:linear-gradient(135deg,#3a4458,#9aa7b8 55%,#d9dde3);clip-path:polygon(0 0,100% 0,100% 79%,78% 100%,0 100%)" role="img" aria-label="Overhead view of business partners shaking hands over a desk with charts and a laptop"></div>
  <h2>Silverbrook Meridian Holdings (SMH)</h2>
  <p>At Silverbrook Meridian Holdings, LLC, we are poised to revolutionize industries by leveraging cutting-edge AI and blockchain technologies. With a bold vision and resilience, we are ready to drive transformative growth and capture unparalleled opportunities in the market.</p>
  <span class="btn" style="left:612px;top:415px;width:155px;height:44px">Read More</span>
</section>

<section class="acquire">
  <h2>Driving Economic Growth<br>Through Strategic Acquisitions</h2>
  <p class="lead">Our strategy targets companies with stable growth potential that are resilient to market disruptions and poised to leverage technological advancements in AI and blockchain.</p>
  <article class="focus-card" style="left:84px">
    <div class="photo" style="background:linear-gradient(120deg,#6b5a48,#c9b7a0 40%,#e05a3a 70%,#8a6fc0)" role="img" aria-label="Piggy bank beside colourful cone-shaped growth charts"></div>
    <h3>Targeting High-Potential Industries<br>for Growth</h3>
  </article>
  <article class="focus-card" style="left:612px">
    <div class="photo" style="background:linear-gradient(110deg,#1f6b4a,#4fae6a 45%,#b8d6b0 70%,#e8c7c2)" role="img" aria-label="Woman reviewing a glowing revenue operations growth chart"></div>
    <h3>Scaling and Optimizing Business Operations for<br>Long-Term Returns</h3>
  </article>
</section>

<section class="services">
  <article class="service" style="left:84px">
    <div class="frame"><div class="photo" style="background:linear-gradient(135deg,#06202c,#0f6a80 55%,#3bc7d8)" role="img" aria-label="Hand on a tablet surrounded by digital security shield icons"></div></div>
    <h3>Cybersecurity</h3>
    <p style="top:262px">Americans and their small to medium-sized businesses are highly vulnerable to increasing cyberattacks, making cybersecurity</p>
    <span class="btn">Read More</span>
  </article>
  <article class="service" style="left:345px">
    <div class="frame"><div class="photo" style="background:linear-gradient(180deg,#2f7fd0,#8fc0ea 55%,#b99a78)" role="img" aria-label="Building under construction with tower cranes against a blue sky"></div></div>
    <h3>Construction and Trade Services</h3>
    <p style="top:262px">ssential trade services like electrical, plumbing, and HVAC are often inefficient and can greatly benefit from technological</p>
    <span class="btn">Read More</span>
  </article>
  <article class="service" style="left:605px">
    <div class="frame"><div class="photo" style="background:linear-gradient(180deg,#7fa9d4,#3a5e80 50%,#2d4a3a)" role="img" aria-label="Modern glass commercial towers at dusk"></div></div>
    <h3>Specialized Commercial Real<br>Estate</h3>
    <p style="top:284px">The growing demand for both physical and data storage solutions presents a significant challenge.</p>
    <span class="btn">Read More</span>
  </article>
  <article class="service" style="left:866px">
    <div class="frame"><div class="photo" style="background:linear-gradient(135deg,#f2f2f0,#e4e1da 50%,#3a3a3a)" role="img" aria-label="Gold coins, glasses, calculator and keyboard on a white desk"></div></div>
    <h3>Digital Assets</h3>
    <p style="top:262px">Treasury assets should actively work for the company rather than sit idle. SMH leverages Corvacoin as a dynamic treasury</p>
    <span class="btn">Read More</span>
  </article>
</section>

<section class="news">
  <h2>News &amp; Insights</h2>
  <span class="rule" style="left:84px;top:252px;width:130px"></span>
  <p class="lead">Etiam at laoreet nunc, at sagittis nibh. Proin efficitur, mauris eget fermentum commodo, eros ante venenatis urna, eget viverra elit justo vitae ante.</p>
  <span class="btn light" style="left:84px;top:422px;width:212px;height:44px">Explore More News</span>
  <article class="post" style="left:464px">
    <span class="edge"></span>
    <div class="photo" style="background:linear-gradient(180deg,#15181d,#3b3a34 60%,#8d7a52)" role="img" aria-label="Hands tending seedlings growing from stacks of coins"></div>
    <time>07.02.2024</time>
    <h3>Etiam at laoreet nunc, at sagittis nibh mauris eget fermentum commodo</h3>
    <p>Americans and their small to medium-sized businesses are highly v increasing cyberattacks, mak eros ante venenatis urna</p>
    <span class="more">LEARN MORE</span>
  </article>
  <article class="post" style="left:806px">
    <span class="edge"></span>
    <div class="photo" style="background:linear-gradient(180deg,#b9cde0,#6f8fb0 55%,#2f4e78)" role="img" aria-label="City skyline with rising blue bar chart and arrow"></div>
    <time>07.02.2024</time>
    <h3>Etiam at laoreet nunc, at sagittis nibh mauris eget fermentum commodo</h3>
    <p>Americans and their small to medium-sized businesses are highly v increasing cyberattacks, mak eros ante venenatis urna</p>
    <span class="more">LEARN MORE</span>
  </article>
</section>

<section class="cta">
  <h2>Invest in Your Future Today</h2>
  <span class="rule"></span>
  <p>Discover high-potential investment opportunities in the Cybersecurity, Trade &amp; Construction Services, and Specialized CRE industries.</p>
  <span class="btn" style="left:783px;top:130px;width:155px;height:44px;border-color:var(--white)">Contact Us</span>
</section>

<footer class="site-footer">
  <div class="fcol" style="left:84px">
    <h4>Private Equity</h4>
    <ul><li>Portfolio</li><li>Our Investing</li><li>Our Impact</li><li>News &amp; Insights</li></ul>
  </div>
  <div class="fcol" style="left:342px">
    <h4>Quick Links</h4>
    <ul><li>Home</li><li>Who We Are</li><li>What We Do</li><li>Portfolio</li><li>Meet The Team</li></ul>
  </div>
  <div class="fcol" style="left:590px">
    <h4>About</h4>
    <ul><li>Contact Us</li><li>More Info</li></ul>
  </div>
  <div class="fcol" style="left:822px">
    <h4>Join Our Monthly Newsletter</h4>
  </div>
  <div class="email">Email address</div>
  <div class="subscribe">SUBSCRIBE</div>

  <div class="brand">
    <span class="brand-mark"></span>
    <span class="brand-name">Silverbrook Meridian<br>Holdings, LLC</span>
  </div>
  <div class="connect">
    <span>STAY CONNECTED :</span><span>CONTACT US</span><span>|</span><span>SUSCBRIBE</span><span>|</span><span>LOCATION</span>
  </div>
  <div class="social"><span></span><span></span><span></span></div>
  <p class="legal">© 2024 <b>Silverbrook Meridian Holdings</b>. All right reserved</p>
</footer>

</body>
</html>
```